Tidal Forge MSP - Power Point Template Creation

I need someone to create a full slide deck template that is branded with logo and follows our color choices that can be used as a template to create presentations from.

```html
<!DOCTYPE html>
<html lang="en">
<head>
<meta charset="utf-8">
<title>Tidal Forge MSP – Slide Deck Template</title>
<link href="https://fonts.googleapis.com/css2?family=Montserrat:ital,wght@0,400;0,500;0,600;0,700;0,800;1,500&display=swap" rel="stylesheet">
<style>
:root{
  --canvas:#e9e9e8;
  --paper:#ffffff;
  --ink:#262626;
  --dark:#232323;
  --grey:#7a7a7a;
  --soft:#f1f1f1;
  --gold:#b88d3b;
  --gold-light:#dcbf6c;
  --gold-grad:linear-gradient(90deg,#a97b2c,#e3c777 50%,#a97b2c);
}
*{margin:0;padding:0;box-sizing:border-box}
html,body{width:900px;height:1200px;overflow:hidden}
body{background:var(--canvas);font-family:'Montserrat',sans-serif;color:var(--ink);position:relative}
.slide{position:absolute;width:272px;height:153px;background:var(--paper);overflow:hidden;box-shadow:0 2px 5px rgba(0,0,0,.18)}
.slide.dark{background:var(--dark)}
.abs{position:absolute}
.wordmark{display:inline-flex;align-items:center;gap:.35em;font-weight:500;white-space:nowrap}
.wordmark::before{content:"";width:.6em;height:.6em;background:var(--gold);flex:none}
.brand{position:absolute;top:6px;right:8px;font-size:3.6px;color:var(--ink)}
.footer-line{position:absolute;left:8px;right:10px;bottom:7px;height:.6px;background:var(--gold)}
.copyright{position:absolute;left:29px;bottom:9px;font-size:2px;color:var(--ink);font-weight:600}
.page-no{position:absolute;right:9px;bottom:3px;font-size:2.6px;color:var(--ink)}
.slide-title{position:absolute;left:10px;top:8px;font-size:9px;font-weight:700;color:var(--ink)}
.title-bar{position:absolute;left:10px;top:21px;width:12px;height:1.4px;background:var(--gold)}
.title-bar::after{content:"";position:absolute;left:13px;top:0;width:1.4px;height:1.4px;background:var(--ink);box-shadow:2.4px 0 0 var(--ink)}
.tiny{font-size:2.6px;line-height:1.35;color:var(--grey)}
.small{font-size:3.4px;line-height:1.4;color:var(--grey)}
.label{font-size:4.4px;font-weight:700;color:var(--ink)}
.label.gold{color:var(--gold)}
.photo{position:absolute}
.gold-fill{background:var(--gold-grad)}
.icon-dot{position:absolute;border-radius:50%;background:radial-gradient(circle,#e6cb7a,#b18532)}
.ring{position:absolute;border-radius:50%;background:#fff;border:1.5px solid var(--gold)}
.ring::after{content:"";position:absolute;inset:3px;border-radius:50%;background:var(--dark)}
</style>
</head>
<body>

<!-- 1 Cover dark -->
<section class="slide dark" style="left:30px;top:35px">
  <div class="photo" role="img" aria-label="Dark moody mountain landscape at dusk" style="inset:0;background:radial-gradient(ellipse at 50% 40%,#4a4a4a,#1c1c1c 70%)"></div>
  <div class="abs" style="left:0;right:0;top:70px;text-align:center;color:#fff;font-size:11px"><span class="wordmark">Tidal Forge MSP</span></div>
</section>

<!-- 2 Title white -->
<section class="slide" style="left:314px;top:35px">
  <div class="abs" style="left:5px;top:5px;width:6px;height:6px;background:var(--gold-light)"></div>
  <div class="abs" style="left:16px;top:31px;font-size:5px"><span class="wordmark">Tidal Forge MSP</span></div>
  <div class="abs" style="left:16px;top:64px;font-size:17px;font-weight:400;line-height:1">BUSINESS</div>
  <div class="abs" style="left:16px;top:83px;font-size:10.5px;font-weight:700;color:var(--gold)">MARKETING</div>
  <div class="abs" style="left:16px;top:99px;width:10px;height:1.2px;background:var(--gold)"></div>
  <div class="abs" style="left:16px;top:107px;font-size:6.5px;font-style:italic;font-weight:500">Presentation</div>
  <div class="abs small" style="left:16px;top:115px;width:80px;font-style:italic">Lorem ipsum dolor sit amet, consectetuer adipiscing elit, sed diam nonum</div>
  <div class="abs" style="left:17px;top:136px;width:3px;height:3px;border-radius:50%;background:var(--gold);box-shadow:5px 0 0 var(--gold),10px 0 0 var(--ink)"></div>
  <div class="photo" role="img" aria-label="Two businesswomen working together at a laptop in a bright office" style="left:114px;top:0;width:158px;height:123px;background:linear-gradient(135deg,#d9dde2,#8d8f94 60%,#2e2e30)"></div>
  <div class="abs gold-fill" style="left:114px;top:123px;width:158px;height:30px"></div>
  <div class="abs" style="left:114px;width:158px;top:136px;text-align:center;font-size:4.2px;letter-spacing:1.6px;color:#fff">WWW.TIDALFORGE.COM</div>
</section>

<!-- 3 Title framed -->
<section class="slide" style="left:598px;top:35px">
  <div class="abs" style="left:5px;top:5px;width:6px;height:6px;background:var(--gold-light)"></div>
  <div class="abs" style="left:16px;top:33px;font-size:5px"><span class="wordmark">Tidal Forge MSP</span></div>
  <div class="abs" style="left:16px;top:66px;font-size:17px;line-height:1">BUSINESS</div>
  <div class="abs" style="left:16px;top:85px;font-size:10.5px;font-weight:700;color:var(--gold)">MARKETING</div>
  <div class="abs" style="left:16px;top:101px;width:10px;height:1.2px;background:var(--gold)"></div>
  <div class="abs" style="left:16px;top:109px;font-size:6.5px;font-style:italic;font-weight:500">Presentation</div>
  <div class="abs small" style="left:16px;top:117px;width:80px;font-style:italic">Lorem ipsum dolor sit amet, consectetuer adipiscing elit, sed diam nonum</div>
  <div class="abs" style="left:17px;top:138px;width:3px;height:3px;border-radius:50%;background:var(--ink);box-shadow:5px 0 0 var(--gold),10px 0 0 var(--ink)"></div>
  <div class="abs gold-fill" style="left:186px;top:0;width:86px;height:36px"></div>
  <div class="abs" style="left:108px;top:118px;width:164px;height:35px;background:var(--dark)"></div>
  <div class="abs" style="left:115px;top:12px;width:150px;height:134px;background:#fff"></div>
  <div class="photo" role="img" aria-label="Two women smiling while reviewing work on a laptop" style="left:122px;top:18px;width:136px;height:122px;background:linear-gradient(135deg,#efe4d8,#c7a98e 55%,#6d5a4c)"></div>
</section>

<!-- 4 Agenda -->
<section class="slide" style="left:30px;top:198px">
  <div class="brand"><span class="wordmark">Tidal Forge MSP</span></div>
  <div class="abs" style="left:47px;top:68px;font-size:14px;font-weight:700">Agenda</div>
  <div class="abs" style="left:122px;top:34px;width:100px">
    <div class="label gold">1. Lorem ipsum</div><div class="tiny" style="padding-left:6px;margin-bottom:8px">Lorem ipsum dolor sit amet, consectetuer adipiscing elit, sed diam nonummy nibh euismod tincid</div>
    <div class="label gold">2. Lorem ipsum</div><div class="tiny" style="padding-left:6px;margin-bottom:8px">Lorem ipsum dolor sit amet, consectetuer adipiscing elit, sed diam nonummy nibh euismod tincid</div>
    <div class="label gold">3. Lorem ipsum</div><div class="tiny" style="padding-left:6px;margin-bottom:8px">Lorem ipsum dolor sit amet, consectetuer adipiscing elit, sed diam nonummy nibh euismod tincid</div>
    <div class="label gold">4. Lorem ipsum</div><div class="tiny" style="padding-left:6px">Lorem ipsum dolor sit amet, consectetuer adipiscing elit, sed diam nonummy nibh euismod tincid</div>
  </div>
  <div class="copyright">Copyright © Tidal Forge MSP LLC</div><div class="footer-line"></div><div class="page-no">2</div>
</section>

<!-- 5 Our Education -->
<section class="slide" style="left:314px;top:198px">
  <div class="brand"><span class="wordmark">Tidal Forge MSP</span></div>
  <div class="slide-title">Our Education</div><div class="title-bar"></div>
  <svg class="abs" style="left:46px;top:36px" width="182" height="74" viewBox="0 0 182 74">
    <g fill="none" stroke="#262626" stroke-width="1.6">
      <rect x="2" y="2" width="52" height="68" rx="5"/>
      <rect x="65" y="2" width="52" height="68" rx="5"/>
      <rect x="128" y="2" width="52" height="68" rx="5"/>
      <path d="M54 60 L65 12"/><path d="M117 60 L128 12"/>
    </g>
    <circle cx="54" cy="60" r="1.8" fill="#262626"/><circle cx="65" cy="12" r="1.8" fill="#262626"/>
    <circle cx="117" cy="60" r="1.8" fill="#262626"/><circle cx="128" cy="12" r="1.8" fill="#262626"/>
    <g fill="none" stroke="#b88d3b" stroke-width=".8">
      <circle cx="28" cy="16" r="3"/><path d="M27 19v2h2v-2"/>
      <rect x="86" y="13" width="10" height="7"/><path d="M86 13l5 4 5-4"/>
      <path d="M150 21v-8M150 21h10M151 19l3-3 2 2 4-4"/>
    </g>
  </svg>
  <div class="abs" style="left:48px;top:60px;width:52px;text-align:center"><div class="label" style="font-size:3.8px">IDEA</div><div class="tiny" style="font-size:2.3px;padding:1px 5px">Lorem ipsum dolor sit amet, consectetuer adipiscing elit, sed diam nonummy nibh euismod tincidunt ut laoreet dolore magna aliquam</div></div>
  <div class="abs" style="left:111px;top:60px;width:52px;text-align:center"><div class="label" style="font-size:3.8px">PROMOTION</div><div class="tiny" style="font-size:2.3px;padding:1px 5px">Lorem ipsum dolor sit amet, consectetuer adipiscing elit, sed diam nonummy nibh euismod tincidunt ut laoreet dolore magna aliquam</div></div>
  <div class="abs" style="left:174px;top:60px;width:52px;text-align:center"><div class="label" style="font-size:3.8px">GROWTH</div><div class="tiny" style="font-size:2.3px;padding:1px 5px">Lorem ipsum dolor sit amet, consectetuer adipiscing elit, sed diam nonummy nibh euismod tincidunt ut laoreet dolore magna aliquam</div></div>
  <div class="abs tiny" style="left:30px;top:116px;width:212px;text-align:center">Lorem ipsum dolor sit amet, consectetuer adipiscing elit, sed diam nonummy nibh euismod tincidunt ut laoreet dolore magna aliquam erat volutpat. Ut wisi enim ad minim veniam, quis nostrud exerci tation ullamcorper suscipit lobortis nisl ut aliquip ex ea commodo consequat.</div>
  <div class="copyright">Copyright © Tidal Forge MSP LLC</div><div class="footer-line"></div><div class="page-no">3</div>
</section>

<!-- 6 Lorem Ipsum team -->
<section class="slide" style="left:598px;top:198px">
  <div class="brand"><span class="wordmark">Tidal Forge MSP</span></div>
  <div class="abs" style="left:12px;top:14px;font-size:8px;font-weight:700;line-height:1.4">Lorem Ipsum<br>Dolor Sit<br>Ametkeeper.</div>
  <div class="title-bar" style="left:12px;top:51px"></div>
  <div class="abs tiny" style="left:12px;top:58px;width:72px;font-size:2.8px">Lorem ipsum dolor sit amet, consectetuer adipiscing elit, sed diam nonummy nibh euismod tincidunt ut laoreet dolore magna aliquam erat volutpat.<br><br>Ut wisi enim ad minim veniam, quis nostrud exerci tation ullamcorper suscipit lobortis nisl ut aliquip ex ea commodo consequat. Duis autem vel eum iriure dolor in hendrerit in vulputate velit esse molestie.<br><br>vel illum dolore eu feugiat nulla facilisis at vero eros et accumsan et iusto odio</div>
  <div class="photo" role="img" aria-label="Team meeting around a long office table" style="left:95px;top:24px;width:177px;height:71px;background:linear-gradient(135deg,#e5e5e3,#9c9c9a 55%,#4b4b4b)"></div>
  <div class="abs" style="left:120px;top:75px;width:44px;height:56px;background:#fff;box-shadow:0 1px 2px rgba(0,0,0,.2)"></div>
  <div class="abs" style="left:119px;top:75px;width:46px;height:13px;background:var(--dark);color:#fff;font-size:7px;font-weight:600;text-align:center;line-height:13px">Text Here</div>
  <div class="abs tiny" style="left:123px;top:91px;width:38px;font-size:2.1px">Lorem ipsum dolor sit amet, consectetuer adipiscing elit, sed diam nonummy nibh euismod tincidunt ut laoreet dolore magna aliquam erat volutpat.<br><br>Ut wisi enim ad minim veniam, quis nostrud exerci tation ullamcorper</div>
  <div class="abs" style="left:185px;top:75px;width:44px;height:56px;background:#fff;box-shadow:0 1px 2px rgba(0,0,0,.2)"></div>
  <div class="abs" style="left:184px;top:75px;width:46px;height:13px;background:var(--dark);color:#fff;font-size:7px;font-weight:600;text-align:center;line-height:13px">Text Here</div>
  <div class="abs tiny" style="left:188px;top:91px;width:38px;font-size:2.1px">Lorem ipsum dolor sit amet, consectetuer adipiscing elit, sed diam nonummy nibh euismod tincidunt ut laoreet dolore magna aliquam erat volutpat.<br><br>Ut wisi enim ad minim veniam, quis nostrud exerci tation ullamcorper</div>
  <div class="copyright">Copyright © Tidal Forge MSP LLC</div><div class="footer-line"></div><div class="page-no">4</div>
</section>

<!-- 7 Values -->
<section class="slide" style="left:30px;top:362px">
  <div class="brand"><span class="wordmark">Tidal Forge MSP</span></div>
  <div class="slide-title">Text Added Hare</div><div class="title-bar"></div>
  <div class="abs tiny" style="left:18px;top:32px;width:44px;font-size:3.2px">Lorem ipsum dolor sit amet,consec-tetuer adipiscing elit, sed diam nonummy nibh euismod tincidunt erat volutpat.<br><br>Ut wisi enim ad minim veniam, quis nostrud exerci tation ullamcorper suscipit lobortis nisl ut aliquip ex ea commodo consequat.</div>
  <div class="photo" role="img" aria-label="Businessman silhouette facing a glowing city window with digital icons" style="left:78px;top:20px;width:82px;height:84px;background:linear-gradient(135deg,#e7c873,#8c6a2a 60%,#2f2a22);clip-path:polygon(30% 0,100% 0,70% 100%,0 100%)"></div>
  <div class="photo" role="img" aria-label="Office interior in dark tones" style="left:62px;top:108px;width:60px;height:30px;background:linear-gradient(135deg,#6a6a6a,#2b2b2b);clip-path:polygon(30% 0,100% 0,70% 100%,0 100%)"></div>
  <div class="ring" style="left:140px;top:33px;width:14px;height:14px"></div>
  <div class="abs" style="left:168px;top:34px"><div class="label" style="font-size:5px">We Before Me</div><div class="tiny" style="width:86px">ipsum dolor sit amet, cons ectetuer adipiscing elit, sed diam nonummy nibh euismod tincidunt ut laoreet</div></div>
  <div class="ring" style="left:125px;top:68px;width:14px;height:14px"></div>
  <div class="abs" style="left:153px;top:70px"><div class="label" style="font-size:5px">We Are Good People</div><div class="tiny" style="width:86px">ipsum dolor sit amet, cons ectetuer adipiscing elit, sed diam nonummy nibh euismod tincidunt ut laoreet dolore magna aliquam erat volutpat.</div></div>
  <div class="ring" style="left:108px;top:105px;width:14px;height:14px"></div>
  <div class="abs" style="left:136px;top:106px"><div class="label" style="font-size:5px">We Work with Heart</div><div class="tiny" style="width:86px">ipsum dolor sit amet, cons ectetuer adipiscing elit, sed diam nonummy nibh euismod tincidunt</div></div>
  <div class="copyright">Copyright © Tidal Forge MSP LLC</div><div class="footer-line"></div><div class="page-no">5</div>
</section>

<!-- 8 Section break -->
<section class="slide" style="left:314px;top:362px">
  <div class="photo" role="img" aria-label="Office meeting scene washed in a warm gold tone" style="left:12px;top:10px;width:248px;height:133px;background:linear-gradient(135deg,#c79b45,#a87b2f 55%,#7e5a1e)"></div>
  <div class="abs" style="left:138px;top:50px;color:#fff;font-size:13px;line-height:1.1"><div style="font-weight:500">Section</div><div style="font-weight:800">Break</div></div>
  <div class="abs" style="left:138px;top:83px;width:92px;color:#fff;font-size:3.6px;line-height:1.3">Lorem ipsum dolor sit amet, consectetuer sed diam nonummy nibh euismod tincid</div>
</section>

<!-- 9 Numbered list + dark panel -->
<section class="slide" style="left:598px;top:362px">
  <div class="brand"><span class="wordmark">Tidal Forge MSP</span></div>
  <div class="slide-title">Text Added Hare</div><div class="title-bar"></div>
  <div class="abs" style="left:30px;top:35px;width:100px">
    <div class="label" style="font-size:3.8px">01. Aliquam Erat Volutpat</div><div class="tiny" style="padding-left:7px;margin-bottom:8px">Lorem ipsum dolor sit amet, consectetuer adipiscing elit, sed diam nonummy nibh euismod</div>
    <div class="label" style="font-size:3.8px">02. Consectetuer Adipiscing Elit</div><div class="tiny" style="padding-left:7px;margin-bottom:8px">Lorem ipsum dolor sit amet, consectetuer adipiscing elit, sed diam nonummy nibh euismod tincidunt ut laoreet</div>
    <div class="label" style="font-size:3.8px">03. Duis Autem Vel Eum</div><div class="tiny" style="padding-left:7px;margin-bottom:8px">Lorem ipsum dolor sit amet, consectetuer adipiscing elit, sed diam nonummy nibh euismod tincidunt.</div>
    <div class="label" style="font-size:3.8px">04. Aliquam Erat Volutpat</div><div class="tiny" style="padding-left:7px">Lorem ipsum dolor sit amet, consectetuer adipiscing elit, sed diam nonummy nibh euismod tincidunt ut laoreet.</div>
  </div>
  <div class="abs" style="left:148px;top:32px;width:93px;height:95px;background:var(--dark)"></div>
  <div class="icon-dot" style="left:138px;top:40px;width:18px;height:18px;border:2px solid #fff"></div>
  <div class="icon-dot" style="left:138px;top:68px;width:18px;height:18px;border:2px solid #fff"></div>
  <div class="icon-dot" style="left:138px;top:98px;width:18px;height:18px;border:2px solid #fff"></div>
  <div class="abs" style="left:164px;top:40px;width:70px;color:#fff"><div style="font-size:5px;font-weight:600">Lorem ipsum</div><div class="tiny" style="color:#ddd">ipsum dolor sit amet, cons ectetuer adipiscing elit, sed diam nonummy nibh euismod tincidunt ut laoreet</div></div>
  <div class="abs" style="left:164px;top:68px;width:70px;color:#fff"><div style="font-size:5px;font-weight:600">Lorem ipsum</div><div class="tiny" style="color:#ddd">ipsum dolor sit amet, cons ectetuer adipiscing elit, sed diam nonummy nibh euismod tincidunt ut laoreet</div></div>
  <div class="abs" style="left:164px;top:98px;width:70px;color:#fff"><div style="font-size:5px;font-weight:600">Lorem ipsum</div><div class="tiny" style="color:#ddd">ipsum dolor sit amet, cons ectetuer adipiscing elit, sed diam nonummy nibh euismod tincidunt</div></div>
  <div class="copyright">Copyright © Tidal Forge MSP LLC</div><div class="footer-line"></div><div class="page-no">7</div>
</section>

<!-- 10 Market chart -->
<section class="slide" style="left:30px;top:526px">
  <div class="brand"><span class="wordmark">Tidal Forge MSP</span></div>
  <div class="abs" style="left:12px;top:12px;font-size:8.5px;font-weight:700;line-height:1.3">Market<br>Opportunities.</div>
  <div class="title-bar" style="left:12px;top:41px"></div>
  <div class="abs" style="left:0;top:51px;width:94px;height:77px;background:var(--soft)"></div>
  <div class="abs small" style="left:12px;top:57px;width:78px;font-size:4px;line-height:1.25">Lorem ipsum dolor sit amet, consectetuer adipiscing elit, sed diam nonummy nibh euismod tincidunt ut laoreet dolore magna aliquam erat volutpat. Ut wisi enim ad minim veniam, quis nostrud exerci tation ullamcorper suscipit lobortis nisl ut aliquip ex ea commodo consequat. Duis autem vel eum iriure dolor in hendrerit i</div>
  <div class="abs" style="left:112px;top:15px;font-size:4.2px;font-weight:500">CONSECTETUER ADIPISCING</div>
  <svg class="abs" style="left:104px;top:24px" width="152" height="72" viewBox="0 0 152 72">
    <g font-family="Montserrat, sans-serif" font-size="4.3" fill="#262626" text-anchor="end">
      <text x="8" y="4">60</text><text x="8" y="14.5">50</text><text x="8" y="25">40</text><text x="8" y="35.5">30</text><text x="8" y="46">20</text><text x="8" y="56.5">10</text><text x="8" y="67">0</text>
    </g>
    <rect x="12" y="2" width="136" height="63" fill="none" stroke="#262626" stroke-width=".5"/>
    <g stroke="#bbb" stroke-width=".3"><line x1="12" y1="12.5" x2="148" y2="12.5"/><line x1="12" y1="23" x2="148" y2="23"/><line x1="12" y1="33.5" x2="148" y2="33.5"/><line x1="12" y1="44" x2="148" y2="44"/><line x1="12" y1="54.5" x2="148" y2="54.5"/></g>
    <rect x="20" y="7.2" width="15" height="57.8" fill="#262626"/>
    <rect x="52" y="31.4" width="15" height="33.6" fill="#c7a35a"/>
    <rect x="85" y="15.6" width="15" height="49.4" fill="#262626"/>
    <rect x="118" y="36.6" width="15" height="28.4" fill="#c7a35a"/>
    <g font-family="Montserrat, sans-serif" font-size="4.3" fill="#262626" text-anchor="middle">
      <text x="27.5" y="71">JAN</text><text x="59.5" y="71">FEB</text><text x="92.5" y="71">MAR</text><text x="125.5" y="71">APR</text>
    </g>
  </svg>
  <div class="abs" style="left:110px;top:108px;width:64px"><div class="label" style="font-size:5px;display:flex;align-items:center;gap:3px"><span style="width:3.5px;height:3.5px;border-radius:50%;background:var(--gold)"></span>Lorem ipsum</div><div class="tiny" style="padding-left:6px">Lorem ipsum dolor sit amet, consectetuer adipiscing elit, sed diam nonummy nibh euismod tincidunt ut laoreet</div></div>
  <div class="abs" style="left:186px;top:108px;width:64px"><div class="label" style="font-size:5px;display:flex;align-items:center;gap:3px"><span style="width:3.5px;height:3.5px;border-radius:50%;background:var(--gold)"></span>Lorem ipsum</div><div class="tiny" style="padding-left:6px">Lorem ipsum dolor sit amet, consectetuer adipiscing elit, sed diam nonummy nibh euismod tincidunt ut laoreet</div></div>
  <div class="copyright">Copyright © Tidal Forge MSP LLC</div><div class="footer-line"></div><div class="page-no">8</div>
</section>

<!-- 11 Four cards -->
<section class="slide" style="left:314px;top:526px">
  <div class="brand"><span class="wordmark">Tidal Forge MSP</span></div>
  <div class="slide-title">Text Added Hare</div><div class="title-bar"></div>
  <div class="abs" style="left:40px;top:45px;width:44px;height:60px;border:1px solid var(--dark)"></div>
  <div class="abs" style="left:91px;top:45px;width:44px;height:60px;border:1px solid var(--gold)"></div>
  <div class="abs" style="left:143px;top:45px;width:44px;height:60px;border:1px solid var(--dark)"></div>
  <div class="abs" style="left:195px;top:45px;width:44px;height:60px;border:1px solid var(--gold)"></div>
  <div class="icon-dot" style="left:55px;top:37px;width:14px;height:14px;border:1.5px solid #fff"></div>
  <div class="icon-dot" style="left:106px;top:37px;width:14px;height:14px;background:var(--dark);border:1.5px solid #fff"></div>
  <div class="icon-dot" style="left:158px;top:37px;width:14px;height:14px;border:1.5px solid #fff"></div>
  <div class="icon-dot" style="left:210px;top:37px;width:14px;height:14px;background:var(--dark);border:1.5px solid #fff"></div>
  <div class="abs" style="left:45px;top:56px;width:36px"><div class="label" style="font-size:4px">Lorem ipsum</div><div class="tiny" style="font-size:2.1px">Lorem ipsum dolor sit amet, cons ectetuer adipiscing elit, sed diam nonummy nibh euismod tincidunt<br><br>ipsum dolor sit amet, cons ectetuer adipiscing elit, sed diam nonummy</div></div>
  <div class="abs" style="left:96px;top:56px;width:36px"><div class="label gold" style="font-size:4px">Lorem ipsum</div><div class="tiny" style="font-size:2.1px">Lorem ipsum dolor sit amet, cons ectetuer adipiscing elit, sed diam nonummy nibh euismod tincidunt<br><br>ipsum dolor sit amet, cons ectetuer adipiscing elit, sed diam nonummy</div></div>
  <div class="abs" style="left:148px;top:56px;width:36px"><div class="label" style="font-size:4px">Lorem ipsum</div><div class="tiny" style="font-size:2.1px">Lorem ipsum dolor sit amet, cons ectetuer adipiscing elit, sed diam nonummy nibh euismod tincidunt<br><br>ipsum dolor sit amet, cons ectetuer adipiscing elit, sed diam nonummy</div></div>
  <div class="abs" style="left:200px;top:56px;width:36px"><div class="label gold" style="font-size:4px">Lorem ipsum</div><div class="tiny" style="font-size:2.1px">Lorem ipsum dolor sit amet, cons ectetuer adipiscing elit, sed diam nonummy nibh euismod tincidunt<br><br>ipsum dolor sit amet, cons ectetuer adipiscing elit, sed diam nonummy</div></div>
  <div class="abs" style="left:40px;top:113px;font-size:8px;font-weight:600">+ 35k</div>
  <div class="abs tiny" style="left:40px;top:126px;width:160px;font-size:2.2px">Lorem ipsum dolor sit amet, consectetuer adipiscing elit, sed diam nonummy nibh euismod tincidunt ut laoreet dolore magna aliquam erat volutpat. Ut wisi enim ad minim veniam, quis nostrud exerci tation ullamcorper.</div>
  <div class="copyright">Copyright © Tidal Forge MSP LLC</div><div class="footer-line"></div><div class="page-no">9</div>
</section>

<!-- 12 Cycle infographic -->
<section class="slide" style="left:598px;top:526px">
  <div class="brand"><span class="wordmark">Tidal Forge MSP</span></div>
  <div class="slide-title">Text Added Hare</div><div class="title-bar"></div>
  <div class="abs tiny" style="left:11px;top:34px;width:78px;font-size:2.8px">Lorem ipsum dolor sit amet, consectetuer adipiscing elit, sed diam nonummy nibh .<br><br>Ut wisi enim ad minim veniam, quis nostrud exerci tation ullamcorper suscipit lobortis. Ut wisi enim ad minim veniam, quis nostrud exerci tation ullamcorper suscipit lobortis. Ut wisi enim ad minim veniam, quis nostrud exerci tation ullamcorper suscipit lobortis.</div>
  <div class="abs" style="left:14px;top:91px;width:64px"><div class="label" style="font-size:3.8px;display:flex;align-items:center;gap:3px"><span style="width:3px;height:3px;border-radius:50%;background:var(--gold)"></span>Lorem Ipsum</div><div class="tiny" style="font-size:2.1px;padding-left:5px">Lorem ipsum dolor sit amet, consectetuer adipiscing elit, sed diam nonummy nibh euismod tincidunt ut laoreet</div></div>
  <div class="abs" style="left:14px;top:110px;width:64px"><div class="label" style="font-size:3.8px;display:flex;align-items:center;gap:3px"><span style="width:3px;height:3px;border-radius:50%;background:var(--gold)"></span>Lorem Ipsum</div><div class="tiny" style="font-size:2.1px;padding-left:5px">Lorem ipsum dolor sit amet, consectetuer adipiscing elit, sed diam nonummy nibh euismod tincidunt ut laoreet</div></div>
  <svg class="abs" style="left:118px;top:26px" width="120" height="115" viewBox="0 0 120 115">
    <path d="M84 12 A46 46 0 1 0 16 80" fill="none" stroke="#262626" stroke-width="2.5" transform="translate(0,0)"/>
    <path d="M12 68 L18 80 L25 70" fill="none" stroke="#262626" stroke-width="2.2"/>
    <path d="M44 100 A40 40 0 0 0 100 72" fill="none" stroke="#262626" stroke-width="2.5"/>
    <circle cx="95" cy="22" r="13" fill="#fff" stroke="#262626" stroke-width="2"/><circle cx="95" cy="22" r="8.5" fill="#c9a452"/>
    <circle cx="108" cy="66" r="10" fill="#fff" stroke="#262626" stroke-width="2"/><circle cx="108" cy="66" r="6.5" fill="#c9a452"/>
    <circle cx="84" cy="100" r="8" fill="#fff" stroke="#262626" stroke-width="1.8"/><circle cx="84" cy="100" r="5" fill="#c9a452"/>
    <circle cx="40" cy="96" r="6" fill="#fff" stroke="#262626" stroke-width="1.6"/><circle cx="40" cy="96" r="3.5" fill="#c9a452"/>
    <g fill="#262626"><rect x="45" y="40" width="2" height="7"/><rect x="48" y="37" width="2" height="10"/><rect x="51" y="42" width="2" height="5"/></g>
    <g font-family="Montserrat, sans-serif" fill="#b88d3b" font-size="3" font-style="italic"><text x="106" y="8">85%</text><text x="86" y="60">80%</text><text x="52" y="93">50%</text><text x="95" y="112">75%</text></g>
  </svg>
  <div class="abs" style="left:150px;top:74px;width:40px;text-align:center"><div class="label" style="font-size:3.8px">MAIN TITLE</div><div class="tiny" style="font-size:1.8px">Lorem ipsum dolor sit amet, cons ectetuer adipiscing elit</div></div>
  <div class="abs" style="left:228px;top:40px;width:38px;text-align:right"><div class="label" style="font-size:3.4px">Your Title</div><div class="tiny" style="font-size:1.8px">Lorem ipsum dolor sit amet, consectetuer adipiscing elit</div></div>
  <div class="abs" style="left:240px;top:84px;width:28px;text-align:right"><div class="label" style="font-size:3.4px">Your Title</div><div class="tiny" style="font-size:1.8px">Lorem ipsum dolor sit amet, adipiscing elit</div></div>
  <div class="abs" style="left:214px;top:122px;width:40px;text-align:right"><div class="label" style="font-size:3.4px">Your Title</div><div class="tiny" style="font-size:1.8px">Lorem ipsum dolor sit amet, consectetuer adipiscing</div></div>
  <div class="abs" style="left:112px;top:112px;width:38px;text-align:right"><div class="label" style="font-size:3.4px">Your Title</div><div class="tiny" style="font-size:1.8px">Lorem ipsum dolor sit amet, consectetuer adipiscing</div></div>
  <div class="copyright">Copyright © Tidal Forge MSP LLC</div><div class="footer-line"></div><div class="page-no">10</div>
</section>

<!-- 13 Three options -->
<section class="slide" style="left:30px;top:691px">
  <div class="brand"><span class="wordmark">Tidal Forge MSP</span></div>
  <div class="slide-title">Text Added Hare</div><div class="title-bar"></div>
  <svg class="abs" style="left:16px;top:64px" width="16" height="28" viewBox="0 0 16 28"><path d="M0 0h7l9 14-9 14H0l9-14z" fill="#ececec"/></svg>
  <div class="photo" role="img" aria-label="Colleagues discussing at a desk with laptops" style="left:64px;top:32px;width:52px;height:60px;background:linear-gradient(135deg,#c8ccd0,#6f6f70 60%,#353535)"></div>
  <div class="photo" role="img" aria-label="Presenter speaking to a team in a modern office" style="left:130px;top:32px;width:52px;height:60px;background:linear-gradient(135deg,#e6e8ea,#9aa0a5 60%,#4b4e52)"></div>
  <div class="photo" role="img" aria-label="Business partners shaking hands" style="left:196px;top:32px;width:52px;height:60px;background:linear-gradient(135deg,#d7dbe0,#7f848a 60%,#2e3034)"></div>
  <div class="abs" style="left:64px;top:92px;width:52px;height:1.5px;background:var(--gold)"></div>
  <div class="abs" style="left:130px;top:92px;width:52px;height:1.5px;background:var(--gold)"></div>
  <div class="abs" style="left:196px;top:92px;width:52px;height:1.5px;background:var(--gold)"></div>
  <div class="abs" style="left:64px;top:96px;width:50px"><div class="label gold" style="font-size:4.4px">First <span style="color:var(--ink)">Option</span></div><div class="tiny" style="font-size:2.2px">Lorem ipsum dolor sit consectetuer adipiscing elit, sed diam nonummy nibh euismod tincidunt ut dolore magna aliquam erat volutpat. Ut wisi enim ad minim veniam, quis nostrud</div></div>
  <div class="abs" style="left:130px;top:96px;width:50px"><div class="label gold" style="font-size:4.4px">Second <span style="color:var(--ink)">Option</span></div><div class="tiny" style="font-size:2.2px">Lorem ipsum dolor sit consectetuer adipiscing elit, sed diam nonummy nibh euismod tincidunt ut dolore magna aliquam erat volutpat. Ut wisi enim ad minim veniam, quis nostrud</div></div>
  <div class="abs" style="left:196px;top:96px;width:50px"><div class="label gold" style="font-size:4.4px">Third <span style="color:var(--ink)">Option</span></div><div class="tiny" style="font-size:2.2px">Lorem ipsum dolor sit consectetuer adipiscing elit, sed diam nonummy nibh euismod tincidunt ut dolore magna aliquam erat volutpat. Ut wisi enim ad minim veniam, quis nostrud</div></div>
  <div class="copyright">Copyright © Tidal Forge MSP LLC</div><div class="footer-line"></div><div class="page-no">11</div>
</section>

<!-- 14 Hub with projects -->
<section class="slide" style="left:314px;top:691px">
  <div class="brand"><span class="wordmark">Tidal Forge MSP</span></div>
  <div class="slide-title">Text Added Hare</div><div class="title-bar"></div>
  <svg class="abs" style="left:26px;top:30px" width="130" height="110" viewBox="0 0 130 110">
    <circle cx="35" cy="49" r="34" fill="#fff" stroke="#262626" stroke-width="2"/>
    <circle cx="35" cy="49" r="29" fill="#262626"/>
    <circle cx="35" cy="49" r="25" fill="#c9a452"/>
    <circle cx="33" cy="47" r="6" fill="none" stroke="#fff" stroke-width="1.2"/><path d="M37 51l5 5" stroke="#fff" stroke-width="1.4"/>
    <g fill="none" stroke="#262626" stroke-width=".7">
      <path d="M66 32 L82 14 H108"/><path d="M72 49 H108"/><path d="M66 66 L82 84 H108"/>
    </g>
  </svg>
  <div class="icon-dot" style="left:135px;top:36px;width:20px;height:20px;border:2px solid #fff;box-shadow:0 0 0 1px var(--dark)"></div>
  <div class="icon-dot" style="left:135px;top:70px;width:20px;height:20px;border:2px solid #fff;box-shadow:0 0 0 1px var(--dark)"></div>
  <div class="icon-dot" style="left:135px;top:105px;width:20px;height:20px;border:2px solid #fff;box-shadow:0 0 0 1px var(--dark)"></div>
  <div class="abs" style="left:163px;top:34px;width:85px"><div class="label" style="font-size:4.6px;font-weight:600">Project name</div><div class="tiny">Lorem ipsum dolor sit amet, nec an dictas equidem appellantur, ut has commune accommodare. Mea illum, ludus soleat idpro.</div></div>
  <div class="abs" style="left:163px;top:68px;width:85px"><div class="label" style="font-size:4.6px;font-weight:600">Project name</div><div class="tiny">Lorem ipsum dolor sit amet, nec an dictas equidem appellantur, ut has commune accommodare. Mea illum, ludus soleat idpro.</div></div>
  <div class="abs" style="left:163px;top:103px;width:85px"><div class="label" style="font-size:4.6px;font-weight:600">Project name</div><div class="tiny">Lorem ipsum dolor sit amet, nec an dictas equidem appellantur, ut has commune accommodare. Mea illum, ludus soleat idpro.</div></div>
  <div class="copyright">Copyright © Tidal Forge MSP LLC</div><div class="footer-line"></div><div class="page-no">12</div>
</section>

<!-- 15 Text grid -->
<section class="slide" style="left:598px;top:691px">
  <div class="brand"><span class="wordmark">Tidal Forge MSP</span></div>
  <div class="slide-title">Text Added Hare</div><div class="title-bar"></div>
  <div class="abs" style="left:20px;top:34px;width:240px;display:grid;grid-template-columns:repeat(3,72px);column-gap:8px;row-gap:8px">
    <div><div class="label gold" style="font-size:4.2px;font-weight:600">1. Text Added Here</div><div class="tiny" style="font-size:2.2px">Lorem ipsum dolor sit amet, cons ectetuer adipiscing elit, sed diam nonummy nibh euismod tincidunt ut laoreet dolore magna aliquam erat volutpat. Ut wisi enim ad minim veniam, quis nostrud exerci tation ullamcorper suscipit lobortis nisl ut aliquip ex ea commodo consequat.<br><br>Lorem ipsum dolor sit amet, consectetuer adipiscing elit, sed diam nonummy nibh euismod tincidunt ut</div></div>
    <div><div class="label gold" style="font-size:4.2px;font-weight:600">1. Text Added Here</div><div class="tiny" style="font-size:2.2px">Lorem ipsum dolor sit amet, cons ectetuer adipiscing elit, sed diam nonummy nibh euismod tincidunt ut laoreet dolore magna aliquam erat volutpat. Ut wisi enim ad minim veniam, quis nostrud exerci tation ullamcorper.<br><br>Lorem ipsum dolor sit amet, consectetuer adipiscing elit, sed diam nonummy nibh euismod tincidunt ut laoreet dolore magna aliquam erat volutpat.</div></div>
    <div><div class="label gold" style="font-size:4.2px;font-weight:600">1. Text Added Here</div><div class="tiny" style="font-size:2.2px">Lorem ipsum dolor sit amet, cons ectetuer adipiscing elit, sed diam nonummy nibh euismod tincidunt ut laoreet dolore magna aliquam erat volutpat.<br><br>Lorem ipsum dolor sit amet, consectetuer adipiscing elit, sed diam nonummy nibh euismod tincidunt ut laoreet dolore magna aliquam erat volutpat. Ut wisi enim ad minim veniam.</div></div>
    <div><div class="label gold" style="font-size:4.2px;font-weight:600">1. Text Added Here</div><div class="tiny" style="font-size:2.2px">Lorem ipsum dolor sit amet, cons ectetuer adipiscing elit, sed diam nonummy nibh euismod tincidunt ut laoreet dolore magna aliquam erat volutpat. Ut wisi enim ad minim veniam, ea commodo consequat.<br><br>Lorem ipsum dolor sit amet, consectetuer adipiscing elit, sed diam nonummy nibh euismod tincidunt ut laoreet.</div></div>
    <div><div class="label gold" style="font-size:4.2px;font-weight:600">1. Text Added Here</div><div class="tiny" style="font-size:2.2px">Lorem ipsum dolor sit amet, cons ectetuer adipiscing elit, sed diam nonummy nibh euismod tincidunt ut laoreet dolore magna aliquam erat volutpat. Ut wisi enim ad minim veniam.<br><br>Lorem ipsum dolor sit amet, consectetuer adipiscing elit, sed diam nonummy nibh euismod tincidunt ut laoreet dolore.</div></div>
    <div><div class="label gold" style="font-size:4.2px;font-weight:600">1. Text Added Here</div><div class="tiny" style="font-size:2.2px">Lorem ipsum dolor sit amet, cons ectetuer adipiscing elit, sed diam nonummy nibh euismod tincidunt ut laoreet dolore magna ea commodo consequat.<br><br>Lorem ipsum dolor sit amet, consectetuer adipiscing elit, sed diam nonummy nibh euismod tincidunt ut laoreet dolore magna aliquam erat volutpat.</div></div>
  </div>
  <div class="copyright">Copyright © Tidal Forge MSP LLC</div><div class="footer-line"></div><div class="page-no">13</div>
</section>

<!-- 16 Timeline -->
<section class="slide" style="left:30px;top:854px">
  <div class="brand"><span class="wordmark">Tidal Forge MSP</span></div>
  <div class="slide-title">Text Added Hare</div><div class="title-bar"></div>
  <svg class="abs" style="left:24px;top:40px" width="226" height="80" viewBox="0 0 226 80">
    <polygon points="4,46 42,46 46,54 0,54" fill="#262626"/>
    <polygon points="46,46 88,46 92,54 42,54" fill="#c9a452"/>
    <polygon points="92,46 134,46 138,54 88,54" fill="#262626"/>
    <polygon points="138,46 180,46 184,54 134,54" fill="#c9a452"/>
    <polygon points="184,46 222,46 226,54 180,54" fill="#262626"/>
    <g stroke="#262626" stroke-width=".8"><line x1="23" y1="36" x2="23" y2="46"/><line x1="112" y1="36" x2="112" y2="46"/><line x1="200" y1="36" x2="200" y2="46"/><line x1="67" y1="54" x2="67" y2="64"/><line x1="156" y1="54" x2="156" y2="64"/></g>
    <g fill="#262626"><circle cx="23" cy="35" r="1.6"/><circle cx="112" cy="35" r="1.6"/><circle cx="200" cy="35" r="1.6"/></g>
    <g fill="#c9a452"><circle cx="67" cy="65" r="1.6"/><circle cx="156" cy="65" r="1.6"/></g>
    <g font-family="Montserrat, sans-serif" font-size="4" font-weight="600" fill="#fff" text-anchor="middle"><text x="23" y="51.5">1990</text><text x="67" y="51.5">2001</text><text x="112" y="51.5">2007</text><text x="156" y="51.5">2012</text><text x="200" y="51.5">2020</text></g>
  </svg>
  <div class="abs" style="left:22px;top:60px;width:50px;text-align:center"><div class="label" style="font-size:4.2px;font-weight:600">Your Title</div><div class="tiny" style="font-size:3px">Refers to a good or service being offered</div></div>
  <div class="abs" style="left:111px;top:60px;width:50px;text-align:center"><div class="label" style="font-size:4.2px;font-weight:600">Your Title</div><div class="tiny" style="font-size:3px">Refers to a good or service being offered</div></div>
  <div class="abs" style="left:199px;top:60px;width:50px;text-align:center"><div class="label" style="font-size:4.2px;font-weight:600">Your Title</div><div class="tiny" style="font-size:3px">Refers to a good or service being offered</div></div>
  <div class="abs" style="left:66px;top:109px;width:50px;text-align:center"><div class="label" style="font-size:4.2px;font-weight:600">Your Title</div><div class="tiny" style="font-size:3px">Refers to a good or service being offered</div></div>
  <div class="abs" style="left:155px;top:109px;width:50px;text-align:center"><div class="label" style="font-size:4.2px;font-weight:600">Your Title</div><div class="tiny" style="font-size:3px">Refers to a good or service being offered</div></div>
  <div class="copyright">Copyright © Tidal Forge MSP LLC</div><div class="footer-line"></div><div class="page-no">14</div>
</section>

<!-- 17 Puzzle circle -->
<section class="slide" style="left:314px;top:854px">
  <div class="brand"><span class="wordmark">Tidal Forge MSP</span></div>
  <div class="slide-title">Text Added Hare</div><div class="title-bar"></div>
  <svg class="abs" style="left:99px;top:38px" width="78" height="78" viewBox="0 0 78 78">
    <path d="M39 39 L39 1 A38 38 0 0 0 1 39 Z" fill="#262626"/>
    <path d="M39 39 L77 39 A38 38 0 0 0 39 1 Z" fill="#c9a452"/>
    <path d="M39 39 L39 77 A38 38 0 0 0 77 39 Z" fill="#262626"/>
    <path d="M39 39 L1 39 A38 38 0 0 0 39 77 Z" fill="#c9a452"/>
    <g stroke="#fff" stroke-width="1.2"><line x1="39" y1="0" x2="39" y2="78"/><line x1="0" y1="39" x2="78" y2="39"/></g>
    <circle cx="39" cy="8" r="3" fill="#c9a452"/><circle cx="70" cy="39" r="3" fill="#262626"/><circle cx="39" cy="70" r="3" fill="#c9a452"/><circle cx="8" cy="39" r="3" fill="#262626"/>
    <circle cx="39" cy="39" r="18" fill="#fff"/>
    <g fill="none" stroke="#fff" stroke-width=".8"><circle cx="22" cy="22" r="3.5"/><circle cx="56" cy="22" r="3.5"/><circle cx="56" cy="56" r="3.5"/><circle cx="22" cy="56" r="3.5"/></g>
    <text x="39" y="37.5" text-anchor="middle" font-family="Montserrat, sans-serif" font-size="6.5" font-weight="700" fill="#262626">Text</text>
    <text x="39" y="45" text-anchor="middle" font-family="Montserrat, sans-serif" font-size="6.5" font-weight="700" fill="#262626">Added</text>
  </svg>
  <div class="abs" style="left:28px;top:40px;width:66px;text-align:right"><div class="label" style="font-size:4.6px;font-weight:600">Text Here</div><div class="tiny" style="font-size:2.5px">Lorem ipsum dolor sit amet, consectetuer adipiscing elit, sed diammy nibh euismod tincidunt ut laoreet dolore</div></div>
  <div class="abs" style="left:182px;top:40px;width:66px"><div class="label" style="font-size:4.6px;font-weight:600">Text Here</div><div class="tiny" style="font-size:2.5px">Lorem ipsum dolor sit amet, consectetuer adipiscing elit, sed diammy nibh euismod tincidunt ut laoreet dolore</div></div>
  <div class="abs" style="left:28px;top:95px;width:66px;text-align:right"><div class="label" style="font-size:4.6px;font-weight:600">Text Here</div><div class="tiny" style="font-size:2.5px">Lorem ipsum dolor sit amet, consectetuer adipiscing elit, sed diammy nibh euismod tincidunt ut laoreet dolore</div></div>
  <div class="abs" style="left:182px;top:95px;width:66px"><div class="label" style="font-size:4.6px;font-weight:600">Text Here</div><div class="tiny" style="font-size:2.5px">Lorem ipsum dolor sit amet, consectetuer adipiscing elit, sed diammy nibh euismod tincidunt ut laoreet dolore</div></div>
  <div class="copyright">Copyright © Tidal Forge MSP LLC</div><div class="footer-line"></div><div class="page-no">15</div>
</section>

<!-- 18 Steps -->
<section class="slide" style="left:598px;top:854px">
  <div class="brand"><span class="wordmark">Tidal Forge MSP</span></div>
  <div class="slide-title">Text Added Hare</div><div class="title-bar"></div>
  <svg class="abs" style="left:26px;top:50px" width="222" height="22" viewBox="0 0 222 22">
    <defs><linearGradient id="stepGold" x1="0" x2="1"><stop offset="0" stop-color="#b48733"/><stop offset=".5" stop-color="#e2c575"/><stop offset="1" stop-color="#b48733"/></linearGradient></defs>
    <polygon points="0,0 40,0 48,11 40,22 0,22 8,11" fill="url(#stepGold)"/>
    <polygon points="43,0 83,0 91,11 83,22 43,22 51,11" fill="#262626"/>
    <polygon points="86,0 126,0 134,11 126,22 86,22 94,11" fill="url(#stepGold)"/>
    <polygon points="129,0 169,0 177,11 169,22 129,22 137,11" fill="#262626"/>
    <polygon points="172,0 212,0 220,11 212,22 172,22 180,11" fill="url(#stepGold)"/>
    <g font-family="Montserrat, sans-serif" font-size="4.6" font-weight="600" fill="#fff" text-anchor="middle"><text x="26" y="12.6">STEP 01</text><text x="69" y="12.6">STEP 02</text><text x="112" y="12.6">STEP 03</text><text x="155" y="12.6">STEP 04</text><text x="198" y="12.6">STEP 05</text></g>
  </svg>
  <div class="abs" style="left:26px;top:80px;width:222px;display:grid;grid-template-columns:repeat(5,1fr);text-align:center">
    <div><div class="label" style="font-size:4.4px;font-weight:500">Project name</div><div class="tiny" style="font-size:2.8px;padding:1px 5px">Lorem Ipsum is simply dummy unknown printer took a galley of type and scrambled it to make.</div></div>
    <div><div class="label" style="font-size:4.4px;font-weight:500">Project name</div><div class="tiny" style="font-size:2.8px;padding:1px 5px">Lorem Ipsum is simply dummy unknown printer took a galley of type and scrambled it to make.</div></div>
    <div><div class="label" style="font-size:4.4px;font-weight:500">Project name</div><div class="tiny" style="font-size:2.8px;padding:1px 5px">Lorem Ipsum is simply dummy unknown printer took a galley of type and scrambled it to make.</div></div>
    <div><div class="label" style="font-size:4.4px;font-weight:500">Project name</div><div class="tiny" style="font-size:2.8px;padding:1px 5px">Lorem Ipsum is simply dummy unknown printer took a galley of type and scrambled it to make.</div></div>
    <div><div class="label" style="font-size:4.4px;font-weight:500">Project name</div><div class="tiny" style="font-size:2.8px;padding:1px 5px">Lorem Ipsum is simply dummy unknown printer took a galley of type and scrambled it to make.</div></div>
  </div>
  <div class="copyright">Copyright © Tidal Forge MSP LLC</div><div class="footer-line"></div><div class="page-no">16</div>
</section>

<!-- 19 Phones -->
<section class="slide" style="left:30px;top:1019px">
  <div class="brand"><span class="wordmark">Tidal Forge MSP</span></div>
  <div class="slide-title">Text Added Hare</div><div class="title-bar"></div>
  <div class="abs tiny" style="left:14px;top:31px;width:86px;font-size:2.9px">Lorem ipsum dolor sit amet, consectetuer adipiscing elit, sed diam nonummy nibh euismod tincidunt ut laoreet dolore magna aliquam erat volutpat. Ut wisi enim ad minim veniam,<br><br>quis nostrud exerci tation ullamcorper suscipit lobortis nisl ut aliquip ex ea commodo consequat. Duis autem vel eum iriure dolor in hendrerit in vulputate velit esse</div>
  <div class="abs" style="left:23px;top:74px;width:88px">
    <div style="display:flex;gap:4px;margin-bottom:6px"><span style="width:8px;height:8px;background:var(--dark);color:#fff;font-size:5px;font-weight:700;text-align:center;line-height:8px;flex:none">1.</span><div><div class="label gold" style="font-size:3.6px;font-weight:600">Lorem ipsum</div><div class="tiny" style="font-size:2.2px">Lorem ipsum dolor sit amet, consectetuer adipiscing elit, sed diam nonummy nibh euismod tincid</div></div></div>
    <div style="display:flex;gap:4px;margin-bottom:6px"><span style="width:8px;height:8px;background:var(--dark);color:#fff;font-size:5px;font-weight:700;text-align:center;line-height:8px;flex:none">2.</span><div><div class="label gold" style="font-size:3.6px;font-weight:600">Lorem ipsum</div><div class="tiny" style="font-size:2.2px">Lorem ipsum dolor sit amet, consectetuer adipiscing elit, sed diam nonummy nibh euismod tincid</div></div></div>
    <div style="display:flex;gap:4px"><span style="width:8px;height:8px;background:var(--dark);color:#fff;font-size:5px;font-weight:700;text-align:center;line-height:8px;flex:none">3.</span><div><div class="label gold" style="font-size:3.6px;font-weight:600">Lorem ipsum</div><div class="tiny" style="font-size:2.2px">Lorem ipsum dolor sit amet, consectetuer adipiscing elit, sed diam nonummy nibh euismod tincid</div></div></div>
  </div>
  <div class="abs" style="left:125px;top:22px;width:32px;height:66px;border:1.5px solid var(--dark);border-radius:4px;padding:8px 3px">
    <div class="label" style="font-size:3.6px;font-weight:600">Lorem ipsum dolor</div>
    <div style="width:9px;height:7px;border:.7px solid var(--gold);margin:5px auto"></div>
    <div class="tiny" style="font-size:1.7px">To introduce the students to the changing landscape of marketing and equip them with knowledge and tools to navigate the digital marketing world.</div>
  </div>
  <div class="abs" style="left:167px;top:43px;width:32px;height:66px;border:1.5px solid var(--dark);border-radius:4px;padding:8px 3px">
    <div class="label" style="font-size:3.6px;font-weight:600">Dolor sit amet, conse</div>
    <div style="width:9px;height:7px;border:.7px solid var(--gold);margin:5px auto"></div>
    <div class="tiny" style="font-size:1.7px">You will learn concepts and ideas in digital marketing as well as how to use different tools and strategies to optimize your digital marketing campaigns.</div>
  </div>
  <div class="abs" style="left:208px;top:64px;width:32px;height:66px;border:1.5px solid var(--dark);border-radius:4px;padding:8px 3px">
    <div class="label" style="font-size:3.6px;font-weight:600">Consec</div>
    <div style="width:9px;height:9px;border:.7px solid var(--gold);border-radius:50%;margin:5px auto"></div>
    <div class="tiny" style="font-size:1.7px">You are required to pass 80% of the evaluation test to obtain the certificate. The evaluation test can only be taken 3 times.</div>
  </div>
  <div class="copyright">Copyright © Tidal Forge MSP LLC</div><div class="footer-line"></div><div class="page-no">17</div>
</section>

<!-- 20 Team -->
<section class="slide" style="left:314px;top:1019px">
  <div class="brand"><span class="wordmark">Tidal Forge MSP</span></div>
  <div class="slide-title">Text Added Hare</div><div class="title-bar"></div>
  <div class="abs" style="left:25px;top:50px;width:226px;display:grid;grid-template-columns:repeat(4,1fr);column-gap:20px;text-align:center">
    <div><div style="height:16px;background:var(--dark)"></div><div role="img" aria-label="Team member portrait" style="width:20px;height:20px;border-radius:50%;background:#c9c9c9;border:1.5px solid #fff;margin:-11px auto 0"></div><div class="label" style="font-size:4.4px;font-weight:600;margin-top:3px">OWEN HALE</div><div class="tiny" style="font-size:2.1px">ipsum dolor sit amet, cons ectetuer adipiscing elit, sed diam nonummy nibh euismod tincidunt<br><br>ut wisi enim ad minim veniam, quis nostrud</div></div>
    <div><div style="height:16px" class="gold-fill"></div><div role="img" aria-label="Team member portrait" style="width:20px;height:20px;border-radius:50%;background:#c9c9c9;border:1.5px solid #fff;margin:-11px auto 0"></div><div class="label" style="font-size:4.4px;font-weight:600;margin-top:3px">ROSA QUINN</div><div class="tiny" style="font-size:2.1px">ipsum dolor sit amet, cons ectetuer adipiscing elit, sed diam nonummy nibh euismod tincidunt<br><br>aliquam erat volutpat. Ut wisi enim ad minim veniam</div></div>
    <div><div style="height:16px;background:var(--dark)"></div><div role="img" aria-label="Team member portrait" style="width:20px;height:20px;border-radius:50%;background:#c9c9c9;border:1.5px solid #fff;margin:-11px auto 0"></div><div class="label" style="font-size:4.4px;font-weight:600;margin-top:3px">OWEN HALE</div><div class="tiny" style="font-size:2.1px">ipsum dolor sit amet, cons ectetuer adipiscing elit, sed diam nonummy nibh euismod tincidunt<br><br>ut wisi enim ad minim veniam, quis nostrud</div></div>
    <div><div style="height:16px" class="gold-fill"></div><div role="img" aria-label="Team member portrait" style="width:20px;height:20px;border-radius:50%;background:#c9c9c9;border:1.5px solid #fff;margin:-11px auto 0"></div><div class="label" style="font-size:4.4px;font-weight:600;margin-top:3px">ROSA QUINN</div><div class="tiny" style="font-size:2.1px">ipsum dolor sit amet, cons ectetuer adipiscing elit, sed diam nonummy nibh euismod tincidunt<br><br>aliquam erat volutpat. Ut wisi enim ad minim veniam</div></div>
  </div>
  <div class="copyright">Copyright © Tidal Forge MSP LLC</div><div class="footer-line"></div><div class="page-no">17</div>
</section>

<!-- 21 Thank you -->
<section class="slide dark" style="left:598px;top:1019px">
  <div class="photo" role="img" aria-label="Dark textured background with faint mechanical detail" style="inset:0;background:radial-gradient(ellipse at 30% 60%,#3a3a3a,#1d1d1d 75%)"></div>
  <div class="abs" style="left:12px;top:84px;width:116px;text-align:center;color:#fff;font-size:8px"><span class="wordmark">Tidal Forge MSP</span></div>
  <div class="abs" style="left:144px;top:36px;font-size:17px;font-weight:800;color:var(--gold-light)">Thank You</div>
  <svg class="abs" style="left:144px;top:66px" width="16" height="64" viewBox="0 0 16 64">
    <path d="M2 1c1 5 4 8 8 9l1.5-2-2-2-1.2 1c-1.5-.7-2.8-2-3.4-3.4l1-1.2-2-2z" fill="#d2b062"/>
    <path d="M1 26l10-4-4 10-1-5z" fill="#d2b062"/>
    <path d="M1 47l6-5 6 5h-1.6v5h-3v-3h-2.8v3h-3v-5z" fill="#d2b062"/>
    <g stroke="#fff" stroke-width=".5"><line x1="14" y1="0" x2="14" y2="10"/><line x1="14" y1="19" x2="14" y2="30"/><line x1="14" y1="40" x2="14" y2="53"/></g>
  </svg>
  <div class="abs" style="left:162px;top:66px;color:#fff;font-size:4.4px;line-height:1.25">+18 2767 5550 1234<br>+18 2767 5550 1234</div>
  <div class="abs" style="left:162px;top:86px;color:#fff;font-size:4.4px;line-height:1.25">www.tidalforge.com<br>hello@tidalforge.com</div>
  <div class="abs" style="left:162px;top:106px;color:#fff;font-size:4.4px;line-height:1.25">88 Harbour Lane, Port Ellis,<br>state/country, post/zip 012345.</div>
</section>

</body>
</html>
```